Create modern and sleek business card for luxury real estate company

We're a "boutique" real estate office looking for a design that gets across a highly modern luxury brand. Blacks and whites are probably the best colors unless we try a silver foil for the logo. I've attached a version of our current logo here. I'd like to swap out the current font on there with Gotham Light Regular.

I'm looking to have one side of the card have the logo with the space for our agents info on the other side.

Target Market(s)

Young professionals in a "luxury" headspace

Industry/Entity Type

Real estate

Contact Information for Business Card

A place for agent name, cell number, website. The slogan "Quietly Elevating Every Home".

Font styles to use
Other font styles liked:
• Gotham Regular

Colors

Designer to choose only greyscale colors for use in the design.

Requirements
Must have
• Matte black as the background color. Clean lines and use of contrast. A specific design aspect that will use silver foil.
Nice to have
• Up in the air on integrating a QR code
Should not have
• Any houses or other real estate related design (ex: a clip art house)

```html
<!DOCTYPE html>
<html lang="en">
<head>
<meta charset="utf-8">
<title>Lumen Realty – Business Card</title>
<link href="https://fonts.googleapis.com/css2?family=Montserrat:wght@300;400&display=swap" rel="stylesheet">
<style>
  :root {
    --backdrop: #808080;
    --card-black: #000000;
    --ink-white: #ffffff;
    --ink-soft: #e6e6e6;
    --ghost: #0d0d0d;
  }
  * { margin: 0; padding: 0; box-sizing: border-box; }
  html, body {
    width: 1146px;
    height: 1200px;
    overflow: hidden;
    background: var(--backdrop);
    font-family: "Montserrat", Arial, sans-serif;
    color: var(--ink-white);
  }
  .card {
    position: absolute;
    left: 223px;
    width: 699px;
    height: 400px;
    background: var(--card-black);
    overflow: hidden;
  }
  .card--front { top: 201px; }
  .card--back  { top: 647px; }

  .ghost-ring {
    position: absolute;
    left: -20px;
    top: 81px;
    width: 312px;
    height: 312px;
    border: 5px solid var(--ghost);
    border-radius: 50%;
  }
  .brand-seal {
    position: absolute;
    display: flex;
    align-items: center;
    justify-content: center;
    border: 4px solid var(--ink-white);
    border-radius: 50%;
    font-weight: 300;
    letter-spacing: 2px;
    color: var(--ink-white);
  }
  .brand-seal--large {
    left: 474px; top: 98px;
    width: 211px; height: 211px;
    font-size: 34px;
    margin-left: -222px;
  }
  .brand-seal--small {
    left: 547px; top: 140px;
    width: 121px; height: 121px;
    border-width: 3px;
    font-size: 20px;
    letter-spacing: 1px;
  }

  .text-line {
    position: absolute;
    white-space: nowrap;
    font-weight: 300;
  }
  .company-name { left: 39px; top: 28px; font-size: 33px; letter-spacing: 2.5px; }
  .tagline { left: 35px; top: 66px; font-size: 16.5px; letter-spacing: 0.8px; color: var(--ink-soft); }
  .agent-name { left: 33px; top: 138px; font-size: 34px; letter-spacing: 2.5px; }
  .agent-role { left: 33px; top: 176px; font-size: 18px; letter-spacing: 1px; color: var(--ink-soft); }

  .contact-list { position: absolute; left: 32px; top: 231px; list-style: none; }
  .contact-item {
    display: flex;
    align-items: center;
    height: 34px;
    font-size: 20.5px;
    font-weight: 300;
    letter-spacing: 1.2px;
    white-space: nowrap;
  }
  .contact-item:last-child { margin-top: 5px; }
  .contact-icon { width: 18px; height: 18px; margin-right: 9px; fill: var(--ink-white); flex: none; }

  .light-rule {
    position: absolute;
    left: 500px;
    top: 36px;
    width: 8px;
    height: 328px;
    background: radial-gradient(ellipse 50% 50% at center, #ffffff 0%, rgba(255,255,255,0.55) 35%, rgba(255,255,255,0.12) 70%, rgba(255,255,255,0) 100%);
  }
</style>
</head>
<body>

<section class="card card--front">
  <div class="ghost-ring"></div>
  <div class="brand-seal brand-seal--large">LUMEN</div>
</section>

<section class="card card--back">
  <p class="text-line company-name">LUMEN REALTY</p>
  <p class="text-line tagline">"Quietly Elevating Every Home"</p>
  <p class="text-line agent-name">DANIEL REYES</p>
  <p class="text-line agent-role">Manager</p>

  <ul class="contact-list">
    <li class="contact-item">
      <svg class="contact-icon" viewBox="0 0 24 24"><path d="M6.6 10.8a15.1 15.1 0 0 0 6.6 6.6l2.2-2.2a1 1 0 0 1 1-.25 11.4 11.4 0 0 0 3.6.57 1 1 0 0 1 1 1V20a1 1 0 0 1-1 1A17 17 0 0 1 3 4a1 1 0 0 1 1-1h3.5a1 1 0 0 1 1 1c0 1.25.2 2.45.57 3.57a1 1 0 0 1-.25 1z"/></svg>
      (123) 456 7890
    </li>
    <li class="contact-item">
      <svg class="contact-icon" viewBox="0 0 24 24"><path d="M12 2a10 10 0 1 0 0 20 10 10 0 0 0 0-20zm6.9 6h-3a15.6 15.6 0 0 0-1.3-3.6A8 8 0 0 1 18.9 8zM12 4c.8 1.2 1.5 2.5 1.9 4h-3.8c.4-1.5 1.1-2.8 1.9-4zM4.3 14a8 8 0 0 1 0-4h3.4a16.5 16.5 0 0 0 0 4zm.8 2h3a15.6 15.6 0 0 0 1.3 3.6A8 8 0 0 1 5.1 16zm3-8h-3a8 8 0 0 1 4.3-3.6A15.6 15.6 0 0 0 8.1 8zM12 20c-.8-1.2-1.5-2.5-1.9-4h3.8c-.4 1.5-1.1 2.8-1.9 4zm2.3-6H9.7a14.7 14.7 0 0 1 0-4h4.6a14.7 14.7 0 0 1 0 4zm.3 5.6a15.6 15.6 0 0 0 1.3-3.6h3a8 8 0 0 1-4.3 3.6zm1.7-5.6a16.5 16.5 0 0 0 0-4h3.4a8 8 0 0 1 0 4z"/></svg>
      YourWebsite.com
    </li>
    <li class="contact-item">
      <svg class="contact-icon" viewBox="0 0 24 24"><path d="M2 5h20v14H2zm2 2v.5l8 5.5 8-5.5V7zm0 3v7h16v-7l-8 5.5z"/></svg>
      Mail@yourwebsite.com
    </li>
    <li class="contact-item">
      <svg class="contact-icon" viewBox="0 0 24 24"><path d="M12 1a8 8 0 0 0-8 8c0 6 8 14 8 14s8-8 8-14a8 8 0 0 0-8-8zm0 11a3 3 0 1 1 0-6 3 3 0 0 1 0 6z"/></svg>
      123 Your Address, Your City, ZIP 12345
    </li>
  </ul>

  <div class="light-rule"></div>
  <div class="brand-seal brand-seal--small">LUMEN</div>
</section>

</body>
</html>
```